Optometrist/Eye Care Clinic Business card with new logo attached

We are a small, independent eye care clinic in Canada. We have recently updated our logo (as attached), and would like a professional, modern and health care oriented business card to highlight our office details and our optometrist. We'd like to incorporate the blue colours as seen on our logo.

Target Market(s)

demographic: age 35-65 male/female equal

Industry/Entity Type

Health Care

Contact Information for Business Card

Name of clinic: "Marrow Bend Eye Care Optometry"

Font styles to use
Sans Serif

Colors
0355a3

Requirements
Must have
• our website: marrowbendeyecare.com
• Dr Lena Quorvik
• Optometrist
• 217-392 E Halvering Ave
• Vancouver BC V6R 3J8
• P: 604-319-2058
• E: info@marrowbendeyecare.com
Nice to have
• front side: logo/name of clinic as seen on logo attached and website
• backside: logo on the left side, and name/title/address/phone/email

```html
<!DOCTYPE html>
<html lang="en">
<head>
<meta charset="utf-8">
<title>Marrow Bend Eye Care Optometry – Business Card</title>
<link rel="stylesheet" href="https://fonts.googleapis.com/css2?family=Open+Sans:wght@400;700&display=swap">
<style>
  :root {
    --backdrop: #5c5c5c;
    --navy: #0b3a55;
    --brand-blue: #0355a3;
    --teal: #1f7fae;
    --white: #ffffff;
  }
  * { box-sizing: border-box; margin: 0; padding: 0; }
  html, body { width: 1200px; height: 802px; overflow: hidden; }
  body {
    background: var(--backdrop);
    font-family: "Open Sans", sans-serif;
    position: relative;
  }
  .card {
    position: absolute;
    top: 274px;
    width: 443px;
    height: 265px;
  }
  .card--contact { left: 136px; background: var(--navy); color: var(--white); overflow: hidden; }
  .card--brand { left: 624px; background: var(--white); }

  .contact-mark {
    position: absolute;
    left: 22px;
    top: 104px;
    width: 170px;
    font-size: 15px;
    font-weight: 400;
    line-height: 1.3;
    color: var(--white);
  }

  .contact-block {
    position: absolute;
    right: 27px;
    top: 100px;
    text-align: right;
    font-size: 13px;
    line-height: 16px;
  }
  .doctor-name { font-size: 17px; font-weight: 700; line-height: 20px; letter-spacing: 0.2px; }
  .doctor-title { margin-bottom: 12px; }
  .address { margin-bottom: 15px; }
  .contact-line { display: flex; justify-content: flex-end; align-items: center; gap: 3px; }
  .contact-line svg { width: 10px; height: 10px; flex: none; }

  .brand-lockup {
    position: absolute;
    left: 0; right: 0;
    top: 96px;
    display: flex;
    flex-direction: column;
    align-items: center;
    gap: 12px;
  }
  .brand-dot {
    width: 34px; height: 34px;
    border-radius: 50%;
    background: var(--brand-blue);
  }
  .brand-name {
    font-size: 18px;
    font-weight: 400;
    letter-spacing: 2px;
    color: var(--brand-blue);
    text-align: center;
    line-height: 1.3;
  }
</style>
</head>
<body>
  <section class="card card--contact">
    <p class="contact-mark">Marrow Bend Eye Care Optometry</p>
    <div class="contact-block">
      <p class="doctor-name">DR LENA QUORVIK</p>
      <p class="doctor-title">Optometrist</p>
      <p class="address">217-392 E Halvering Ave<br>Vancouver BC V6R 3J8</p>
      <p class="contact-line">604-319-2058
        <svg viewBox="0 0 10 10" aria-hidden="true"><path fill="#fff" d="M1 3.5C1 2 2.5 1.5 5 1.5S9 2 9 3.5L7.3 4 7 3H3L2.7 4ZM3 4.5h4l1 4H2Z"/></svg>
      </p>
      <p class="contact-line">info@marrowbendeyecare.com
        <svg viewBox="0 0 10 10" aria-hidden="true"><rect x="0.5" y="2" width="9" height="6.5" fill="#fff"/><path d="M0.8 2.3 5 5.8 9.2 2.3" fill="none" stroke="#0b3a55" stroke-width="0.9"/></svg>
      </p>
      <p class="contact-line">www.marrowbendeyecare.com
        <svg viewBox="0 0 10 10" aria-hidden="true"><circle cx="5" cy="5" r="4.5" fill="#fff"/><path d="M3 3.5c1 0 1.5 1 2.5 1S6 6.5 4.5 7M6.5 2.5c.5.8 1.5.8 2 1.5" fill="none" stroke="#0b3a55" stroke-width="0.9"/></svg>
      </p>
    </div>
  </section>

  <section class="card card--brand">
    <div class="brand-lockup">
      <span class="brand-dot" aria-hidden="true"></span>
      <p class="brand-name">MARROW BEND<br>EYE CARE OPTOMETRY</p>
    </div>
  </section>
</body>
</html>
```